NEW Website DESIGN for Brightwell Panes & Stoneworks Company

Brand New website, contemporary, clean, visual (images), not busy. ATTACHED IS OUR LOG THAT YOU MUST USE.

The company is called Brightwell Panes & Stoneworks (BrightwellPS)
www.brightwellps.com
The website should be www.brightwellpns.com
one page for glass one page for solid surfaces www.brightwellpanesplashes.co.uk
www.brightwellstoneworkss.co.uk

Target Market(s)

Hotels, Commercial projects, Small focus on residential

Industry/Entity Type

Construction

Number of Pages Required

5+ page

Font styles to use
Sans Serif

Requirements
Must have
• COLOURS AS PER OUR LOGO - WHITE/YELLOW/GREY - WHITE BACK GROUND
• CLEAR SIMPLE NAVIGATION - MODER CLEAN CUT - DESIGN FEEL
• LATEST NAVIGATION FOR IMAGES and text to include per project details
• WORK/PROJECT AREA - NEWS AREA - TEAM AREA/ABOUT US/CONTACT US
• NEW PAGEwww.brightwellpanesplashes.co.uk - NEW PAGE www.brightwellstoneworkss.co.uk
• PLEASE COPY THIS TYPE OF TEMPALTE
• https://www.harlowmead.co.uk/project/grand-halls/
• MOBILE READY
• WORDPRESS
• MODERN IMAGES INCLUDING VELMARA KESTRIN AND GLASS PROJECTS
Nice to have
• NEW DESIGN MODER FRESH
• WEBSITES I LIKE THE TEMPLATE SHOULD BE LIKE THE WEBSITE BELOW
• https://www.harlowmead.co.uk/
Should not have
• NOT Old fashion template, not busy NAVIGATION
• NO BLACK
• NO DARK GREYS
• NOT LOTS OF YELLOW
• RESDENTIAL IMAGES

```html
<!DOCTYPE html>
<html lang="en">
<head>
<meta charset="utf-8">
<title>Brightwell Panes & Stoneworks</title>
<link href="https://fonts.googleapis.com/css2?family=Montserrat:wght@600;700;800;900&family=Open+Sans:wght@400;600;700&display=swap" rel="stylesheet">
<style>
:root{
  --yellow:#f3a712;
  --yellow-soft:#fbe7b5;
  --grey:#8c8c8c;
  --grey-mid:#a9a9a9;
  --grey-light:#eeeeee;
  --text:#5a5a5a;
  --heading:#555555;
  --white:#ffffff;
}
*{box-sizing:border-box;margin:0;padding:0}
html,body{width:1200px;height:3336px;overflow:hidden;background:var(--white)}
body{font-family:"Open Sans",Arial,sans-serif;color:var(--text);font-size:13px;position:relative}
h1,h2,h3,h4,.btn,.nav a{font-family:"Montserrat",Arial,sans-serif}
.btn{display:inline-block;background:var(--yellow);color:var(--white);font-weight:700;font-size:11px;letter-spacing:.5px;padding:9px 18px;text-transform:uppercase}
section,header,footer,nav{position:absolute;left:0;width:1200px}
.ph{display:block}

/* header */
.site-header{top:0;height:88px;background:var(--white)}
.brand{position:absolute;left:150px;top:14px;display:flex;align-items:center;gap:10px}
.brand-dot{width:44px;height:44px;border-radius:50%;background:var(--yellow)}
.brand-name{font-family:"Montserrat",sans-serif;font-weight:700;font-size:14px;color:var(--heading);line-height:1.2;width:150px}
.contact-top{position:absolute;right:260px;top:12px;text-align:left}
.contact-top small{display:block;color:var(--yellow);font-weight:700;font-size:10px;letter-spacing:1px}
.contact-top strong{display:block;font-family:"Montserrat",sans-serif;font-size:20px;color:var(--heading)}
.contact-top span{font-size:11px}
.socials{position:absolute;right:150px;top:50px;display:flex;gap:5px}
.socials i{width:22px;height:22px;background:var(--grey)}

/* nav */
.nav{top:88px;height:48px;background:var(--grey);display:flex;align-items:center;padding-left:150px}
.nav a{color:var(--white);text-decoration:none;font-weight:700;font-size:12px;padding:0 24px;line-height:48px}
.nav a.active{background:var(--yellow)}
.nav .enquiry{position:absolute;right:150px;top:9px;line-height:30px;padding:0 16px;background:var(--yellow)}

/* hero */
.hero{top:136px;height:464px;background:linear-gradient(120deg,#9b9a93 0%,#c9c7bf 40%,#e9e7e1 70%,#bdbab0 100%)}
.hero-copy{position:absolute;left:0;right:0;top:110px;text-align:center;color:var(--white)}
.hero-copy h1{font-size:46px;font-weight:900;line-height:1.05;text-shadow:0 2px 6px rgba(80,80,80,.5)}
.hero-copy p{width:560px;margin:18px auto 24px;font-size:13px;line-height:1.6;text-shadow:0 1px 3px rgba(80,80,80,.6)}
.dots{position:absolute;bottom:18px;left:0;right:0;display:flex;justify-content:center;gap:6px}
.dots i{width:9px;height:9px;border-radius:50%;background:var(--white);opacity:.6}
.dots i:first-child{opacity:1}

/* work */
.work{top:600px;height:560px}
.work-band{position:absolute;top:0;left:0;width:1200px;height:440px;background:var(--yellow)}
.section-title{text-align:center;font-weight:900;font-size:34px;color:var(--heading);text-transform:uppercase}
.section-title::after{content:"";display:block;width:60px;height:3px;background:var(--yellow);margin:10px auto 0}
.work .section-title{position:absolute;top:40px;width:100%;color:var(--white)}
.work .section-title::after{background:var(--white)}
.cards{position:absolute;top:120px;left:176px;display:flex;gap:16px}
.card{width:200px;height:400px;background:var(--white);box-shadow:0 2px 8px rgba(120,120,120,.25);text-align:center}
.card .ph{height:130px}
.card h3{font-size:13px;font-weight:800;color:var(--heading);margin:16px 12px 10px;text-transform:uppercase;line-height:1.3}
.card p{font-size:11px;line-height:1.55;padding:0 14px;height:110px}
.card .btn{font-size:10px;padding:7px 14px}

/* welcome */
.welcome{top:1160px;height:420px}
.welcome-deco{position:absolute;left:0;top:30px;width:180px;height:330px;background:linear-gradient(135deg,#f4f4f4,#dedede)}
.welcome-copy{position:absolute;left:200px;top:60px;width:440px}
.welcome-copy h2{font-size:26px;font-weight:900;color:var(--heading);line-height:1.1;text-transform:uppercase}
.welcome-copy h2::after{content:"";display:block;width:50px;height:3px;background:var(--yellow);margin-top:10px}
.welcome-copy p{margin-top:16px;font-size:12px;line-height:1.7}
.welcome-frame{position:absolute;left:690px;top:70px;width:330px;height:250px;background:var(--yellow)}
.welcome-img{position:absolute;left:670px;top:50px;width:330px;height:250px;background:linear-gradient(135deg,#e7e7e7,#c9c3c6 50%,#d5346f 52%,#e58aa8 70%,#f0f0f0)}

/* estimates */
.estimates{top:1580px;height:120px;background:linear-gradient(90deg,var(--yellow-soft),#fff6dd 60%,var(--yellow-soft))}
.est-icon{position:absolute;left:440px;top:34px;width:52px;height:52px;border-radius:50%;background:var(--yellow)}
.est-copy{position:absolute;left:510px;top:34px;width:340px}
.est-copy h3{font-size:22px;font-weight:900;color:var(--heading)}
.est-copy p{font-size:11px;line-height:1.5;margin-top:4px}
.estimates .btn{position:absolute;left:880px;top:44px}

/* team */
.team{top:1700px;height:460px;background:linear-gradient(180deg,#f1f1f1,#e2e2e2)}
.team .section-title{position:absolute;top:36px;width:100%}
.members{position:absolute;top:120px;left:190px;display:flex;gap:20px}
.member{width:190px;height:200px;position:relative;background:linear-gradient(180deg,#d8d8d8,#bdbdbd)}
.member figcaption{position:absolute;left:0;right:0;bottom:0;background:rgba(110,110,110,.85);color:var(--white);padding:6px 10px;font-size:11px;line-height:1.3}
.member figcaption b{display:block;font-size:12px}
.team-text{position:absolute;top:340px;left:190px;width:820px;font-size:11px;line-height:1.6;text-align:left}
.team .btn{position:absolute;top:400px;left:190px}

/* news & reviews */
.news{top:2180px;height:540px}
.news-col{position:absolute;left:190px;top:30px;width:380px}
.news-head{display:flex;justify-content:space-between;align-items:center}
.news-head h2{font-size:26px;font-weight:900;color:var(--heading)}
.news-head .btn{padding:6px 12px;font-size:10px}
.news-head + hr{border:0;height:3px;width:50px;background:var(--yellow);margin:8px 0 20px}
.news-item{display:flex;gap:14px;margin-bottom:22px}
.news-item .ph{width:110px;height:80px;flex:none;background:linear-gradient(135deg,#cfd8c4,#9fae93)}
.news-item small{display:block;font-size:10px;color:var(--grey)}
.news-item em{display:block;font-style:normal;color:var(--yellow);font-weight:700;font-size:11px;margin-top:2px}
.news-item h4{font-size:14px;font-weight:700;color:var(--heading);margin-top:3px;line-height:1.3}
.news-item p{font-size:11px;margin-top:3px}
.reviews{position:absolute;left:600px;top:30px;width:410px;height:420px;background:var(--grey-light)}
.reviews .ph{position:absolute;right:0;top:0;width:210px;height:420px;background:linear-gradient(160deg,#f2efe9,#d9cfc2 60%,#c8b9a6)}
.reviews-copy{position:absolute;left:22px;top:24px;width:230px}
.reviews-copy h2{font-size:24px;font-weight:900;color:var(--heading);line-height:1.1}
.reviews-copy h2::after{content:"";display:block;width:50px;height:3px;background:var(--yellow);margin-top:10px}
.quote-mark{font-family:"Montserrat",sans-serif;font-size:48px;color:var(--yellow);line-height:1;margin-top:14px}
.reviews-copy p{font-size:11px;line-height:1.6}
.reviews-copy cite{display:block;margin-top:12px;font-style:normal;font-weight:700;font-size:11px;color:var(--heading)}
.rdots{display:flex;gap:5px;margin-top:16px}
.rdots i{width:8px;height:8px;border-radius:50%;background:var(--grey-mid)}
.rdots i:first-child{background:var(--yellow)}

/* map & form */
.locate{top:2740px;height:460px}
.locate .map{position:absolute;inset:0;background:linear-gradient(135deg,#e9ebe5,#dfe6ee 40%,#eee9dc 70%,#e4e9e0)}
.pin-card{position:absolute;left:290px;top:110px;width:190px;background:var(--white);padding:12px;box-shadow:0 2px 6px rgba(120,120,120,.3);font-size:10px;line-height:1.4}
.pin-card b{display:block;color:var(--yellow);font-size:11px}
.quote-form{position:absolute;left:760px;top:40px;width:250px;height:380px;background:var(--white);box-shadow:0 2px 10px rgba(120,120,120,.3)}
.quote-form h3{background:var(--grey);color:var(--white);font-size:14px;font-weight:900;text-align:center;padding:16px 10px}
.field{margin:12px 18px 0;border:1px solid #d6d6d6;height:30px;font-size:10px;color:#9a9a9a;padding:8px}
.field.area{height:70px}
.quote-form .btn{margin:14px 18px 0;font-size:10px}

/* footer */
.site-footer{top:3200px;height:136px;background:var(--grey-mid);color:var(--white)}
.foot-nav{display:flex;justify-content:center;gap:44px;height:32px;align-items:center;background:var(--grey);font-family:"Montserrat",sans-serif;font-weight:700;font-size:11px}
.foot-col{position:absolute;top:46px;font-size:11px;line-height:1.5}
.foot-col b{display:flex;align-items:center;gap:6px;font-family:"Montserrat",sans-serif;font-size:12px}
.foot-loc{left:190px}
.foot-phone{right:190px;text-align:left}
.foot-brand{position:absolute;left:0;right:0;top:40px;text-align:center;font-family:"Montserrat",sans-serif;font-weight:700;font-size:12px}
.foot-brand .brand-dot{display:block;width:30px;height:30px;margin:0 auto 4px;background:var(--white)}
.foot-social{display:flex;gap:5px;justify-content:center;margin-top:6px}
.foot-social i{width:20px;height:20px;background:var(--white)}
.copyright{position:absolute;bottom:4px;left:0;right:0;text-align:center;font-size:9px}
</style>
</head>
<body>

<header class="site-header">
  <div class="brand"><span class="brand-dot"></span><span class="brand-name">Brightwell Panes &amp; Stoneworks</span></div>
  <div class="contact-top">
    <small>CONTACT US NOW</small>
    <strong>+44 (0)207 555 0148</strong>
    <span>info@brightwellps.com</span>
  </div>
  <div class="socials"><i></i><i></i><i></i><i></i></div>
</header>

<nav class="nav">
  <a class="active">HOME</a><a>ABOUT</a><a>WORK</a><a>NEWS</a><a>TEAM</a><a>CONTACT</a>
  <a class="enquiry">ENQUIRY FORM</a>
</nav>

<section class="hero">
  <div class="ph" role="img" aria-label="Modern kitchen with glass splashback and plants" style="position:absolute;inset:0"></div>
  <div class="hero-copy">
    <h1>GLASS SPLASHBACKS<br>DESIGNED BY YOU</h1>
    <p>Bespoke glass splashbacks cut and finished to your exact colour and size, giving any kitchen, bathroom or hotel space a clean, bright and modern look that lasts.</p>
    <span class="btn">GET IN TOUCH FOR A QUOTE</span>
  </div>
  <div class="dots"><i></i><i></i><i></i><i></i></div>
</section>

<section class="work">
  <div class="work-band"></div>
  <h2 class="section-title">OUR WORK</h2>
  <div class="cards">
    <article class="card">
      <div class="ph" role="img" aria-label="Velmara solid surface worktop project" style="background:linear-gradient(135deg,#e8e8e8,#c8c8c8)"></div>
      <h3>Bespoke Velmara</h3>
      <p>Velmara surfaces moulded to your layout, seamless joins and hard-wearing finishes for hotels and commercial spaces.</p>
      <span class="btn">READ MORE</span>
    </article>
    <article class="card">
      <div class="ph" role="img" aria-label="Glass worktop and splashback in a pink kitchen" style="background:linear-gradient(135deg,#f0dbe4,#d45a8a)"></div>
      <h3>Contemporary Glass Worktops and Splashbacks</h3>
      <p>Toughened glass in any colour, made to measure and fitted by our own team for a clean modern finish.</p>
      <span class="btn">READ MORE</span>
    </article>
    <article class="card">
      <div class="ph" role="img" aria-label="Large mirror in a bright bathroom" style="background:linear-gradient(135deg,#eef0f2,#b9c2c9)"></div>
      <h3>Beautiful Mirrors</h3>
      <p>Made-to-measure mirrors with polished edges and lighting options, ideal for hotel suites and receptions.</p>
      <span class="btn">READ MORE</span>
    </article>
    <article class="card">
      <div class="ph" role="img" aria-label="Wet room with glass shower screen" style="background:linear-gradient(135deg,#e4e4e4,#9f9f9f)"></div>
      <h3>Wet Rooms</h3>
      <p>Frameless glass screens and solid surface panels for wet rooms that are easy to clean and built to last.</p>
      <span class="btn">READ MORE</span>
    </article>
  </div>
</section>

<section class="welcome">
  <div class="welcome-deco" role="img" aria-label="Decorative grey triangle pattern"></div>
  <div class="welcome-copy">
    <h2>Welcome to Brightwell<br>Panes &amp; Stoneworks</h2>
    <p>We design, make and install glass and solid surface products for hotels, commercial projects and selected homes. Every piece is cut to size in our own workshop and fitted by our trained installers.</p>
    <p>From splashbacks and worktops to wet rooms and mirrors, we work with architects and contractors to deliver on time, on budget and with a finish that stays looking new for years to come.</p>
  </div>
  <div class="welcome-frame"></div>
  <div class="welcome-img" role="img" aria-label="White kitchen with magenta glass splashback"></div>
</section>

<section class="estimates">
  <span class="est-icon"></span>
  <div class="est-copy">
    <h3>GET YOUR FREE ESTIMATES</h3>
    <p>Send us your sizes and ideas and we will reply with a clear, no-obligation quote within two working days.</p>
  </div>
  <span class="btn">CONTACT US</span>
</section>

<section class="team">
  <h2 class="section-title">MEET OUR TEAM</h2>
  <div class="members">
    <figure class="member" role="img" aria-label="Portrait of Marcus Leland"><figcaption><b>Marcus Leland</b>Director</figcaption></figure>
    <figure class="member" role="img" aria-label="Portrait of Owen Pryce"><figcaption><b>Owen Pryce</b>Project Manager</figcaption></figure>
    <figure class="member" role="img" aria-label="Portrait of Daniel Achter"><figcaption><b>Daniel Achter</b>Lead Installer</figcaption></figure>
    <figure class="member" role="img" aria-label="Portrait of Reece Hollis"><figcaption><b>Reece Hollis</b>Sales Manager</figcaption></figure>
  </div>
  <p class="team-text">Our small, experienced team handles every job from first visit to final fit. We are always keen to meet skilled fabricators and installers who share our care for quality work.</p>
  <span class="btn">JOIN OUR TEAM</span>
</section>

<section class="news">
  <div class="news-col">
    <div class="news-head"><h2>LATEST NEWS</h2><span class="btn">VIEW ALL</span></div>
    <hr>
    <article class="news-item">
      <div class="ph" role="img" aria-label="Office building photo"></div>
      <div><small>18 JUNE 2024 / NEWS</small><em>Company News</em><h4>Spotlight on… our virtual office</h4><p>A look at how we run projects remotely.</p></div>
    </article>
    <article class="news-item">
      <div class="ph" role="img" aria-label="Green glass worktop" style="background:linear-gradient(135deg,#d8e9c8,#86b06a)"></div>
      <div><small>02 JUNE 2024 / PROJECTS</small><em>Finished Projects</em><h4>Glass Worktops in Ashford Green</h4><p>A bright new finish for a busy kitchen.</p></div>
    </article>
    <article class="news-item">
      <div class="ph" role="img" aria-label="Charity ribbon" style="background:linear-gradient(135deg,#efe6f4,#8a5aa6)"></div>
      <div><small>21 MAY 2024 / EVENTS</small><em>Events</em><h4>Fundraising for the Little Amos Trust</h4><p>Our team took on a sponsored walk.</p></div>
    </article>
  </div>
  <div class="reviews">
    <div class="ph" role="img" aria-label="Happy family in their new kitchen"></div>
    <div class="reviews-copy">
      <h2>HAPPY CUSTOMER<br>REVIEWS</h2>
      <div class="quote-mark">“</div>
      <p>From the first call to the final fit the team were friendly, tidy and quick. Our new glass splashback looks fantastic and the price was exactly as quoted. We would happily recommend them to anyone.</p>
      <cite>Sarah Milton</cite>
      <div class="rdots"><i></i><i></i><i></i><i></i></div>
    </div>
  </div>
</section>

<section class="locate">
  <div class="map" role="img" aria-label="Street map showing the workshop location"></div>
  <div class="pin-card"><b>Brightwell Panes &amp; Stoneworks</b>Unit 4, Meridian Park, Harlow Road, Essex CM19 5QT</div>
  <form class="quote-form">
    <h3>GET IN TOUCH FOR A QUOTE</h3>
    <div class="field">Your Name</div>
    <div class="field">Your Email Address</div>
    <div class="field">Your Phone Number</div>
    <div class="field area">Your Message</div>
    <span class="btn">SEND US A MESSAGE</span>
  </form>
</section>

<footer class="site-footer">
  <div class="foot-nav"><span>HOME</span><span>ABOUT</span><span>NEWS</span><span>TEAM</span><span>CONTACT</span></div>
  <div class="foot-col foot-loc">
    <b><svg width="12" height="16" viewBox="0 0 12 16"><path d="M6 0a6 6 0 0 0-6 6c0 4.5 6 10 6 10s6-5.5 6-10a6 6 0 0 0-6-6zm0 8.5A2.5 2.5 0 1 1 6 3.5a2.5 2.5 0 0 1 0 5z" fill="#fff"/></svg>OUR LOCATION</b>
    Unit 4, Meridian Park<br>Harlow Road, Essex<br>CM19 5QT
  </div>
  <div class="foot-brand">
    <span class="brand-dot"></span>
    Brightwell Panes &amp; Stoneworks
    <div class="foot-social"><i></i><i></i><i></i><i></i></div>
  </div>
  <div class="foot-col foot-phone">
    <b><svg width="14" height="14" viewBox="0 0 24 24"><path d="M6.6 10.8a15 15 0 0 0 6.6 6.6l2.2-2.2c.3-.3.7-.4 1-.2 1.1.4 2.3.6 3.6.6.6 0 1 .4 1 1V20c0 .6-.4 1-1 1A17 17 0 0 1 3 4c0-.6.4-1 1-1h3.5c.6 0 1 .4 1 1 0 1.3.2 2.5.6 3.6.1.3 0 .7-.2 1z" fill="#fff"/></svg>PHONE</b>
    +44 (0)207 555 0148
  </div>
  <div class="copyright">© Brightwell Panes &amp; Stoneworks</div>
</footer>

</body>
</html>
```